Computer repair company needs door hanger type flyer designed

Our company name is Brindlefen Technical Solutions. We are a PC and Mac repair company located in Laguna Niguel, CA. We provide services to all of South Orange County. We fix things like slow computers, errors, virus infections, data recovery, backups, data recovery, wireless networks, printing, helpdesk, onsite and remote support. With this flyer, we want to advertise that we will fix any problem in office for $99. some restrictions apply. We also offer free pickup and delivery. We would like our Quorra and Pinwheelia logo's, as well. I have included our logo in adobe illustrator format. our website address is www.brindlefenit.example.

please use one of the template files included for sizing.
Updates

I have uploaded a template for the size and shape of the door hanger. Please use this for accurate sizing. Also, designs should be for front only. I would also like to add a line that says "We offer business services, too! Visit our website for details."

Industry/Entity Type

Computer

```html
<!DOCTYPE html>
<html lang="en">
<head>
<meta charset="utf-8">
<title>Brindlefen Technical Solutions – Door Hanger</title>
<link rel="stylesheet" href="https://fonts.googleapis.com/css2?family=Orbitron:wght@500;900&family=Oswald:wght@400;500;700&family=Advent+Pro:wght@300;400&display=swap">
<style>
  :root {
    --ink: #000000;
    --paper: #ffffff;
    --accent-cyan: #19e3ec;
    --silver: #d6d6d6;
    --silver-shade: #6a6a6a;
    --display-font: "Orbitron", sans-serif;
    --body-font: "Oswald", sans-serif;
    --script-font: "Advent Pro", sans-serif;
  }
  html, body {
    margin: 0;
    padding: 0;
    width: 1200px;
    height: 3106px;
    overflow: hidden;
    background: var(--paper);
  }
  .door-hanger { display: block; width: 1200px; height: 3106px; }
  .brand-name { font-family: var(--display-font); font-weight: 900; fill: var(--ink); }
  .brand-tagline { font-family: var(--body-font); font-weight: 400; fill: var(--ink); }
  .band-label { font-family: var(--script-font); font-weight: 400; fill: var(--paper); }
  .service-headline { font-family: var(--body-font); font-weight: 400; fill: var(--ink); }
  .service-list { font-family: var(--body-font); font-weight: 400; fill: var(--ink); }
  .price-top { font-family: var(--body-font); font-weight: 700; fill: var(--silver); }
  .price-depth { font-family: var(--body-font); font-weight: 700; fill: var(--silver-shade); }
  .offer-label { font-family: var(--script-font); font-weight: 300; fill: var(--paper); }
  .free-top { font-family: var(--body-font); font-weight: 700; fill: var(--silver); }
  .free-depth { font-family: var(--body-font); font-weight: 700; fill: var(--silver-shade); }
  .badge-name { font-family: var(--body-font); font-weight: 500; fill: var(--ink); }
  .business-note { font-family: var(--body-font); font-weight: 500; fill: var(--ink); }
  .web-address { font-family: var(--display-font); font-weight: 500; fill: var(--paper); }
</style>
</head>
<body>
<svg class="door-hanger" viewBox="0 0 1200 3106" xmlns="http://www.w3.org/2000/svg">
  <defs>
    <linearGradient id="halftoneTone" x1="0" y1="0" x2="0" y2="1">
      <stop offset="0" stop-color="#1a1a1a"/>
      <stop offset="0.55" stop-color="#8a8a8a"/>
      <stop offset="1" stop-color="#ffffff"/>
    </linearGradient>
  </defs>

  <!-- header texture & hanger hole -->
  <rect class="header-texture" x="0" y="0" width="1200" height="540" fill="url(#halftoneTone)" role="img" aria-label="Halftone dot pattern fading from black to white"/>
  <rect class="accent-line" x="0" y="290" width="450" height="9" fill="var(--accent-cyan)"/>
  <circle class="hanger-hole" cx="600" cy="250" r="165" fill="var(--paper)" stroke="var(--ink)" stroke-width="6"/>

  <!-- brand -->
  <text class="brand-name" x="600" y="779" text-anchor="middle" font-size="285" textLength="1110" lengthAdjust="spacingAndGlyphs">BRINDLEFEN</text>
  <text class="brand-tagline" x="600" y="985" text-anchor="middle" font-size="100" textLength="1090" lengthAdjust="spacingAndGlyphs" letter-spacing="14">TECHNICAL SOLUTIONS</text>

  <!-- we fix band -->
  <polygon class="fix-band" points="12,1082 1118,1082 1118,1162 0,1162 0,1094" fill="var(--ink)"/>
  <text class="band-label" x="600" y="1146" text-anchor="middle" font-size="76" font-style="italic" letter-spacing="4">We Fix</text>

  <!-- services -->
  <text class="service-headline" font-size="96">
    <tspan x="44" y="1300" textLength="660" lengthAdjust="spacingAndGlyphs">SLOW COMPUTERS,</tspan>
    <tspan x="44" y="1415" textLength="456" lengthAdjust="spacingAndGlyphs">ERRORS, VIRUS</tspan>
    <tspan x="44" y="1530" textLength="355" lengthAdjust="spacingAndGlyphs">INFECTIONS</tspan>
  </text>

  <circle class="price-disc" cx="906" cy="1362" r="176" fill="var(--ink)"/>
  <g class="price" text-anchor="middle" font-size="200">
    <text class="price-depth" x="921" y="1450" aria-hidden="true">$99</text>
    <text class="price-depth" x="916" y="1445" aria-hidden="true">$99</text>
    <text class="price-depth" x="911" y="1440" aria-hidden="true">$99</text>
    <text class="price-top" x="901" y="1432">$99</text>
  </g>

  <text class="service-list" font-size="34">
    <tspan x="42" y="1625" textLength="1116" lengthAdjust="spacing">DATA RECOVERY, BACKUPS, WIRELESS NETWORKS, PRINTING, HELPDESK, ONSITE</tspan>
    <tspan x="42" y="1678">AND REMOTE SUPPORT.</tspan>
  </text>

  <rect class="divider" x="0" y="1712" width="1200" height="5" fill="var(--ink)"/>

  <!-- free pickup section -->
  <rect class="offer-panel" x="0" y="1735" width="1200" height="820" fill="var(--ink)"/>
  <text class="offer-label" x="600" y="1875" text-anchor="middle" font-size="140" textLength="990" lengthAdjust="spacingAndGlyphs">Pickup &amp; Delivery</text>

  <g class="free" text-anchor="middle" font-size="630">
    <text class="free-depth" x="622" y="2465" textLength="940" lengthAdjust="spacingAndGlyphs" aria-hidden="true">FREE</text>
    <text class="free-depth" x="616" y="2458" textLength="940" lengthAdjust="spacingAndGlyphs" aria-hidden="true">FREE</text>
    <text class="free-depth" x="610" y="2451" textLength="940" lengthAdjust="spacingAndGlyphs" aria-hidden="true">FREE</text>
    <text class="free-depth" x="604" y="2444" textLength="940" lengthAdjust="spacingAndGlyphs" aria-hidden="true">FREE</text>
    <text class="free-top" x="596" y="2436" textLength="940" lengthAdjust="spacingAndGlyphs">FREE</text>
  </g>

  <polygon class="offer-curve" points="0,2488 600,2585 1200,2525 1200,2620 0,2620" fill="var(--paper)"/>

  <!-- brand badge -->
  <circle class="brand-badge" cx="600" cy="2699" r="182" fill="var(--paper)" stroke="var(--ink)" stroke-width="6"/>
  <text class="badge-name" x="600" y="2722" text-anchor="middle" font-size="66">brindlefen</text>

  <!-- footer -->
  <text class="business-note" x="600" y="2912" text-anchor="middle" font-size="38" textLength="1110" lengthAdjust="spacing">WE OFFER BUSINESS SERVICES TOO! VISIT OUR WEBSITE FOR DETAILS:</text>
  <rect class="footer-band" x="0" y="2941" width="1200" height="165" fill="var(--ink)"/>
  <text class="web-address" x="600" y="3048" text-anchor="middle" font-size="56" textLength="1090" lengthAdjust="spacing">WWW.BRINDLEFENIT.EXAMPLE</text>
</svg>
</body>
</html>
```